Redesign wellness clinic website

The project is redesign a wellness clinic http://www.thornleighvitality.example. The new website is to be responsive,clean,bright and a strong call to action which is to book an appointment. The logo will remain the same but the colour scheme on the website should be reflect purple white and green. I want it to be bright and cheerful and the feeling of clarity. The website shouldn't be overloaded with content but more visuals.

Target Market(s)

Anyone that has corporate wellness benefits within the downtown Toronto core. Majority of audience are professional working in Media, Telecommunications and Investments.

Industry/Entity Type

Health And Wellness

Number of Pages Required

5+ page

Font styles to use
Sans Serif

Colors
ffffff
886aae
acd036

Requirements
Must have
• -Strong call to action which is book an appointment like this page https://www.kestrelmotion.example/
• -Services provided icons on the page like https://www.brightpathvitalityhouse.example/
• - Pictures of a good visualizing a fit and healthy life
• - Strong ratings from Quorva, Zintrel, PostMaz, similar to this website http://www.summitbalancehealth.example/our-team-professionals/
• - Bright and clear
Should not have
• -No black and white images (redo our pictures)
• -Dark themes

```html
<!DOCTYPE html>
<html lang="en">
<head>
<meta charset="utf-8">
<title>Thornleigh Vitality Centre – Responsive Home</title>
<link rel="stylesheet" href="https://fonts.googleapis.com/css2?family=Open+Sans:wght@400;600;700&display=swap">
<style>
  :root{
    --purple:#886aae;
    --purple-deep:#6f4f9c;
    --green:#acd036;
    --white:#ffffff;
    --canvas:#ffffff;
    --hero-a:#b9c6e8;
    --hero-b:#8f9fd6;
    --hero-skin:#e2b796;
    --hero-towel:#f1f0f4;
    --menu-a:#a17cc9;
    --menu-b:#7d5aa8;
    --menu-c:#6b4b98;
  }
  *{box-sizing:border-box;margin:0;padding:0}
  html,body{width:1200px;height:1200px;overflow:hidden;background:var(--canvas)}
  body{position:relative;font-family:"Open Sans",sans-serif;color:var(--white)}

  .screen{position:absolute;overflow:hidden;background:var(--white)}
  .screen--desktop{left:201px;top:83px;width:804px;height:502px}
  .screen--mobile{top:752px;width:206px;height:364px;border:1px solid #d9d6df}
  .screen--home{left:342px}
  .screen--menu{left:664px}

  .site-header{position:absolute;left:0;top:0;width:100%;background:var(--white);display:flex;align-items:center}
  .hamburger{position:absolute;display:block}
  .brand{position:absolute;left:50%;transform:translateX(-50%);display:flex;flex-direction:column;align-items:center;color:var(--purple);font-weight:400;white-space:nowrap}
  .brand__dot{border-radius:50%;background:var(--green)}
  .btn-book{position:absolute;background:var(--purple);color:var(--white);font-weight:600;display:flex;align-items:center;justify-content:center;border-radius:12px 3px 12px 3px;white-space:nowrap}

  .hero{position:absolute;left:0;width:100%;
    background:
      linear-gradient(180deg,rgba(255,255,255,0) 60%,var(--hero-towel) 100%),
      radial-gradient(ellipse 45% 35% at 62% 55%,var(--hero-skin) 0%,rgba(226,183,150,0) 100%),
      radial-gradient(ellipse 35% 40% at 18% 30%,#f4f2f5 0%,rgba(244,242,245,0) 100%),
      linear-gradient(120deg,var(--hero-a) 0%,var(--hero-b) 100%)}
  .hero__copy{position:absolute;left:0;width:100%;text-align:center;text-shadow:0 1px 4px rgba(60,50,90,.45)}
  .hero__title{font-weight:700}
  .hero__name{font-weight:600}
  .hero__tag{font-weight:600}
  .hero .btn-book{left:50%;transform:translateX(-50%)}
  .hero__phone{position:absolute;left:50%;transform:translateX(-50%);display:flex;align-items:center;color:var(--purple);font-weight:700;white-space:nowrap}

  /* desktop */
  .screen--desktop .site-header{height:70px}
  .screen--desktop .hamburger{left:122px;top:27px}
  .screen--desktop .brand{top:14px;font-size:8px;gap:4px}
  .screen--desktop .brand__dot{width:30px;height:30px}
  .screen--desktop .site-header .btn-book{left:552px;top:22px;width:138px;height:25px;font-size:9px}
  .screen--desktop .hero{top:70px;height:432px}
  .screen--desktop .hero__title{position:absolute;top:70px;width:100%;font-size:37px;letter-spacing:9px}
  .screen--desktop .hero__name{position:absolute;top:132px;width:100%;font-size:22px;letter-spacing:3px}
  .screen--desktop .hero__tag{position:absolute;top:168px;width:100%;font-size:16px;letter-spacing:5px}
  .screen--desktop .hero .btn-book{top:261px;width:183px;height:33px;font-size:14px}
  .screen--desktop .hero__phone{top:390px;font-size:13px;gap:6px}

  /* mobile home */
  .screen--home .site-header{height:28px}
  .screen--home .hamburger{left:13px;top:10px}
  .screen--home .brand{top:2px;font-size:3px;gap:1px}
  .screen--home .brand__dot{width:14px;height:14px}
  .screen--home .site-header .btn-book{left:137px;top:9px;width:56px;height:9px;font-size:3px;border-radius:4px 1px 4px 1px}
  .screen--home .hero{top:28px;height:336px}
  .screen--home .hero__title{position:absolute;top:70px;width:100%;font-size:19px;letter-spacing:4px}
  .screen--home .hero__name{position:absolute;top:99px;width:100%;font-size:10px;letter-spacing:.6px}
  .screen--home .hero__tag{position:absolute;top:116px;width:100%;font-size:7px;letter-spacing:1.8px}
  .screen--home .hero .btn-book{top:270px;width:133px;height:24px;font-size:10px;border-radius:8px 2px 8px 2px}
  .screen--home .hero__phone{top:304px;font-size:9px;gap:4px}

  /* mobile menu */
  .menu{position:absolute;inset:0;
    background:
      radial-gradient(ellipse 60% 35% at 75% 25%,rgba(214,175,235,.8) 0%,rgba(214,175,235,0) 100%),
      radial-gradient(ellipse 50% 30% at 20% 45%,rgba(190,150,220,.55) 0%,rgba(190,150,220,0) 100%),
      linear-gradient(180deg,var(--menu-a) 0%,var(--menu-b) 55%,var(--menu-c) 100%)}
  .menu__close{position:absolute;left:15px;top:7px}
  .menu__list{list-style:none;position:absolute;left:0;top:56px;width:100%}
  .menu__item{height:33px;display:flex;align-items:center;justify-content:center;font-size:13.5px;letter-spacing:1.2px;color:var(--white)}
  .menu__item--current{height:24px;background:var(--white);color:var(--green);font-weight:600;margin-bottom:9px}
</style>
</head>
<body>

<section class="screen screen--desktop" aria-label="Desktop home page">
  <header class="site-header">
    <svg class="hamburger" width="22" height="16" viewBox="0 0 22 16" aria-label="Menu"><g fill="var(--purple)"><rect y="0" width="22" height="3" rx="1"/><rect y="6.5" width="22" height="3" rx="1"/><rect y="13" width="22" height="3" rx="1"/></g></svg>
    <div class="brand"><span class="brand__dot"></span><span>thornleigh vitality centre</span></div>
    <a class="btn-book">Book an Appointment</a>
  </header>
  <div class="hero" role="img" aria-label="Photo: massage therapist working on a relaxed client lying on a towel, spa stones and bottles beside">
    <div class="hero__copy">
      <h1 class="hero__title">WELCOME</h1>
      <p class="hero__name">THORNLEIGH VITALITY CENTRE</p>
      <p class="hero__tag">Many Disciplines, One Philosophy</p>
    </div>
    <a class="btn-book">Book an Appointment</a>
    <div class="hero__phone">
      <svg width="12" height="20" viewBox="0 0 12 20"><path d="M9 1 C3 2 1 6 1 10 C1 14 3 18 9 19 L10 15 C7 14 6 12 6 10 C6 8 7 6 10 5 Z" fill="var(--green)"/></svg>
      <span>416-555-0187</span>
    </div>
  </div>
</section>

<section class="screen screen--mobile screen--home" aria-label="Mobile home page">
  <header class="site-header">
    <svg class="hamburger" width="13" height="9" viewBox="0 0 22 16" aria-label="Menu"><g fill="var(--purple)"><rect y="0" width="22" height="3" rx="1"/><rect y="6.5" width="22" height="3" rx="1"/><rect y="13" width="22" height="3" rx="1"/></g></svg>
    <div class="brand"><span class="brand__dot"></span><span>thornleigh vitality centre</span></div>
    <a class="btn-book">Book an Appointment</a>
  </header>
  <div class="hero" role="img" aria-label="Photo: massage therapist working on a relaxed client lying on a towel">
    <div class="hero__copy">
      <h1 class="hero__title">WELCOME</h1>
      <p class="hero__name">THORNLEIGH VITALITY CENTRE</p>
      <p class="hero__tag">Many Disciplines, One Philosophy</p>
    </div>
    <a class="btn-book">Book an Appointment</a>
    <div class="hero__phone">
      <svg width="8" height="14" viewBox="0 0 12 20"><path d="M9 1 C3 2 1 6 1 10 C1 14 3 18 9 19 L10 15 C7 14 6 12 6 10 C6 8 7 6 10 5 Z" fill="var(--green)"/></svg>
      <span>416-555-0187</span>
    </div>
  </div>
</section>

<section class="screen screen--mobile screen--menu" aria-label="Mobile navigation menu">
  <nav class="menu" role="img" aria-label="Background photo: soft purple blossoms">
    <svg class="menu__close" width="10" height="10" viewBox="0 0 10 10" aria-label="Close"><path d="M1 1 L9 9 M9 1 L1 9" stroke="var(--white)" stroke-width="1.8" stroke-linecap="round"/></svg>
    <ul class="menu__list">
      <li class="menu__item menu__item--current">Home</li>
      <li class="menu__item">News and Updates</li>
      <li class="menu__item">Corporate Wellness</li>
      <li class="menu__item">Services</li>
      <li class="menu__item">Our Staff</li>
      <li class="menu__item">Forms</li>
      <li class="menu__item">Contact</li>
      <li class="menu__item">Search</li>
    </ul>
  </nav>
</section>

</body>
</html>
```